New Signage Design Project

Hi Corwin, you undertook some design work for our business (business card design) about 12 months ago and we would now like to develop signage for our business using this design. The signage design we are looking for is square in shape and will cover a large area approximately 1.6m x 1.6m.

I'm hoping this will be quite straight forward. We are looking to fill out/extent the background (vertically and out) so that it will suit a square sign.

```html
<!DOCTYPE html>
<html lang="en">
<head>
<meta charset="utf-8">
<title>Ascend Salvage – Square Sign</title>
<link rel="stylesheet" href="https://fonts.googleapis.com/css2?family=Montserrat:wght@500&display=swap">
<style>
  :root {
    --page: #f4f5f6;
    --navy: #2e5270;
    --navy-soft: #5f7b93;
    --white: #ffffff;
  }
  html, body {
    margin: 0;
    padding: 0;
    width: 837px;
    height: 1200px;
    overflow: hidden;
    background: var(--page);
  }
  .canvas {
    position: relative;
    width: 837px;
    height: 1200px;
  }
  .sign {
    position: absolute;
    left: 38px;
    top: 220px;
    width: 760px;
    height: 760px;
    background: var(--navy);
    overflow: hidden;
  }
  .sign__pattern {
    position: absolute;
    inset: 0;
    width: 100%;
    height: 100%;
  }
  .wordmark {
    position: absolute;
    left: 0;
    right: 0;
    top: 300px;
    text-align: center;
    color: var(--white);
    font-family: "Montserrat", sans-serif;
    font-weight: 500;
    line-height: 1;
  }
  .wordmark__primary {
    display: block;
    font-size: 92px;
    letter-spacing: 0.22em;
    margin-right: -0.22em;
  }
  .wordmark__secondary {
    display: block;
    margin-top: 26px;
    font-size: 44px;
    letter-spacing: 0.42em;
    margin-right: -0.42em;
  }
</style>
</head>
<body>
<main class="canvas">
  <section class="sign">
    <svg class="sign__pattern" viewBox="0 0 760 760" role="img" aria-label="Soft ring of pale blue splash shapes framing the sign background">
      <defs>
        <radialGradient id="ringGlow" cx="50%" cy="50%" r="62%">
          <stop offset="0%" stop-color="#2e5270"/>
          <stop offset="58%" stop-color="#2e5270"/>
          <stop offset="80%" stop-color="#4a6884"/>
          <stop offset="100%" stop-color="#5f7b93"/>
        </radialGradient>
      </defs>
      <rect width="760" height="760" fill="url(#ringGlow)"/>
    </svg>
    <h1 class="wordmark">
      <span class="wordmark__primary">ASCEND</span>
      <span class="wordmark__secondary">SALVAGE</span>
    </h1>
  </section>
</main>
</body>
</html>
```